Vorlin Diecast Velcor Collectables Website

looking for a vibrant web site marketplace built for diecast car enthusiasts to buy, sell, and trade with ease. Whether you're looking to showcase your own collection or discover rare and exciting models, our site makes the process simple and enjoyable. Clients can browse a curated inventory of high‑quality diecast cars, connect with fellow collectors, and find the perfect pieces to expand their collection. With a smooth user experience and a community-driven spirit, we’re the go‑to destination for anyone passionate about diecast cars.

Target Market(s)

diecast collectors

Industry/Entity Type

Diecast Collectables

Coding

Coded - Design and coding required

Number of Pages Required

3 page

Font styles to use
Sans Serif

Colors
EE7325
F08F49
F5BC92
FAE3D3
FDF4ED

Requirements
Must have
• Cool look and feel. Woo commerce page to post and sell my inventory
Nice to have
• page for users to post their cars or looking for trades.
Should not have
• look cheap

```html
<!DOCTYPE html>
<html lang="en">
<head>
<meta charset="utf-8">
<title>Vorlin Diecast — The Home of Serious Diecast Fans</title>
<link href="https://fonts.googleapis.com/css2?family=Lato:ital,wght@0,300;0,400;0,700;0,900;1,400&display=swap" rel="stylesheet">
<style>
:root{
  --orange:#EE7325;
  --orange-mid:#F08F49;
  --peach:#F5BC92;
  --blush:#FAE3D3;
  --cream:#FDF4ED;
  --orange-dark:#C95A14;
  --ink:#1E1E1E;
  --muted:#555;
  --white:#fff;
}
*{margin:0;padding:0;box-sizing:border-box}
html,body{width:1200px;height:3584px;overflow:hidden}
body{font-family:'Lato',sans-serif;color:var(--ink);background:var(--white);position:relative}
.heading{font-family:'Lato',sans-serif;font-weight:900;letter-spacing:-.2px}
.abs{position:absolute}
.btn{position:absolute;display:flex;align-items:center;justify-content:center;background:var(--orange);color:var(--white);border-radius:26px;font-weight:700;font-size:17px}
.rule{position:absolute;height:4px;background:var(--orange-mid);border-radius:2px}

/* header + hero */
.hero{position:absolute;left:0;top:0;width:1200px;height:684px;background:radial-gradient(ellipse at 55% 40%,#b23a2a 0%,#6e3324 30%,#4a2a1c 60%,#2a1a12 100%)}
.nav-bar{position:absolute;left:111px;top:24px;width:978px;height:84px;background:var(--white);border-radius:42px}
.brand{position:absolute;left:108px;top:3px;width:125px;height:125px;border-radius:50%;background:var(--white);display:flex;align-items:center;justify-content:center;text-align:center;font-weight:700;font-size:16px;line-height:1.2;color:var(--orange-dark);box-shadow:0 2px 6px rgba(0,0,0,.15)}
.nav-links{position:absolute;left:329px;top:55px;display:flex;gap:27px;font-size:15px;font-weight:700;color:var(--ink)}
.hero-box{position:absolute;left:193px;top:395px;width:830px;height:240px;background:rgba(25,20,18,.62);border-radius:6px}
.hero-title{position:absolute;left:0;width:1200px;top:404px;text-align:center;font-size:46px;color:var(--white)}
.hero-sub{position:absolute;left:0;width:1200px;top:490px;text-align:center;font-size:17px;line-height:28px;color:var(--white)}

/* features */
.feature{position:absolute;top:769px;width:228px;height:243px;background:var(--white);border-radius:10px;box-shadow:0 2px 10px rgba(0,0,0,.13);text-align:center}
.feature svg{margin-top:16px}
.feature h3{font-size:17px;font-weight:700;line-height:28px;margin-top:8px}
.feature p{font-size:14.5px;color:var(--muted);line-height:26px;margin-top:8px}
.feature a{display:block;font-size:14px;font-style:italic;color:#444;text-decoration:underline;margin-top:6px}

/* centerpiece */
.centerpiece{position:absolute;left:0;top:1098px;width:1200px;height:561px;background:var(--cream)}
.h2{font-size:34px;color:var(--orange)}
.body-copy{position:absolute;left:111px;width:446px;font-size:14.5px;line-height:27.5px;color:#333;text-align:justify}
.photo-red{position:absolute;left:642px;top:1183px;width:447px;height:392px;border-radius:12px;background:radial-gradient(ellipse at 55% 60%,#8a1a22 0%,#3a0d14 40%,#140608 100%)}

/* featured */
.product{position:absolute;top:1845px;width:305px;height:354px;background:var(--white);border-radius:14px;box-shadow:0 2px 10px rgba(0,0,0,.12);text-align:center}
.product .pic{height:206px;border-radius:14px 14px 0 0;background:linear-gradient(#fafafa,#f1f1f1)}
.product h3{font-weight:900;font-size:19px;margin-top:18px}
.product .sub{font-size:15px;color:#444;margin-top:12px}
.product .price{font-size:19px;font-weight:700;color:var(--orange);margin-top:10px}

/* cta */
.cta{position:absolute;left:0;top:2308px;width:1200px;height:390px;background:linear-gradient(rgba(238,115,37,.93),rgba(238,115,37,.93)),linear-gradient(#7a3a12,#f08f49)}

/* testimonials */
.review{position:absolute;top:2885px;height:184px;background:var(--white);border-radius:8px;box-shadow:0 2px 10px rgba(0,0,0,.13);text-align:center}
.review h4{font-size:17px;font-weight:700;margin-top:30px}
.stars{color:var(--orange-mid);font-size:15px;letter-spacing:1px;margin-top:2px}
.review p{font-size:14.5px;line-height:25.5px;color:#444;margin:6px auto 0;width:400px}
.quote{position:absolute;right:22px;top:10px;font-weight:900;font-size:44px;color:var(--peach);line-height:1}

/* footer */
.footer{position:absolute;left:0;top:3154px;width:1200px;height:430px;background:var(--orange);color:var(--white)}
.f-brand{position:absolute;left:111px;top:89px;width:125px;height:125px;border-radius:50%;background:var(--white);display:flex;align-items:center;justify-content:center;text-align:center;font-weight:700;font-size:16px;line-height:1.2;color:var(--orange-dark)}
.f-col{position:absolute;top:88px}
.f-col h5{font-weight:300;font-size:19px}
.f-col ul{list-style:none;margin-top:10px}
.f-col li{font-size:14.5px;height:34.4px;display:flex;align-items:center}
.f-col li::before{content:"";width:7px;height:7px;border-radius:50%;background:var(--white);margin:0 14px 0 4px}
.f-contact div{display:flex;font-size:14.5px;line-height:22px;margin-bottom:14px}
.f-contact svg{flex:none;margin:3px 10px 0 0}
.social{position:absolute;top:291px;width:20px;height:20px;border-radius:50%;border:2px solid var(--white)}
.f-line{position:absolute;left:111px;top:377px;width:978px;height:1px;background:rgba(255,255,255,.55)}
.f-bottom{position:absolute;top:396px;font-size:14.5px}
</style>
</head>
<body>

<header class="hero" role="img" aria-label="Close-up photo of a red convertible diecast car among silver and green model cars on a wooden shelf"></header>
<div class="nav-bar"></div>
<div class="brand">Vorlin<br>Diecast</div>
<nav class="nav-links"><span>Home</span><span>Inventory</span><span>Buy</span><span>Sell</span><span>Trade</span><span>Community</span><span>Blog</span><span>FAQ</span><span>Contact Us</span></nav>
<svg class="abs" style="left:997px;top:54px" width="24" height="24" viewBox="0 0 24 24" fill="none" stroke="#111" stroke-width="2.2"><circle cx="10" cy="10" r="7"/><path d="M15 15l6 6"/></svg>
<svg class="abs" style="left:1038px;top:54px" width="20" height="22" viewBox="0 0 20 22" fill="#111"><circle cx="10" cy="6" r="5"/><path d="M1 22c0-6 4-9 9-9s9 3 9 9z"/></svg>

<div class="hero-box"></div>
<h1 class="hero-title heading">The Home of Serious Diecast Fans</h1>
<p class="hero-sub">Buy, sell, and trade rare diecast cars with collectors who value detail,<br>authenticity, and craftsmanship as much as you do.</p>
<div class="btn" style="left:484px;top:571px;width:231px;height:45px">Browse our Inventory</div>

<!-- features -->
<section>
  <div class="feature" style="left:111px">
    <svg width="56" height="56" viewBox="0 0 56 56"><path d="M28 3l7 5 8-1 3 8 7 5-3 8 3 8-7 5-3 8-8-1-7 5-7-5-8 1-3-8-7-5 3-8-3-8 7-5 3-8 8 1z" fill="var(--orange)"/><path d="M18 28l7 7 13-14" stroke="#fff" stroke-width="4" fill="none"/></svg>
    <h3>Verified Collector<br>Listings</h3>
    <p>Every listing is reviewed for<br>accuracy, with clear photos</p>
    <a>Read More</a>
  </div>
  <div class="feature" style="left:361px">
    <svg width="56" height="56" viewBox="0 0 56 56"><circle cx="17" cy="15" r="10" fill="var(--orange)"/><rect x="28" y="28" width="20" height="18" fill="var(--peach)"/><rect x="34" y="8" width="14" height="12" fill="none" stroke="var(--orange)" stroke-width="3"/><rect x="8" y="34" width="14" height="12" fill="none" stroke="var(--orange-mid)" stroke-width="3"/></svg>
    <h3>Buy &nbsp;Sell &nbsp;Trade in<br>One Place</h3>
    <p>Every listing is reviewed for<br>accuracy, with clear photos</p>
    <a>Read More</a>
  </div>
  <div class="feature" style="left:611px">
    <svg width="60" height="56" viewBox="0 0 60 56"><rect x="4" y="10" width="38" height="24" rx="3" fill="var(--orange)"/><rect x="10" y="18" width="38" height="24" rx="3" fill="var(--peach)"/><rect x="10" y="23" width="38" height="5" fill="var(--orange)"/><circle cx="48" cy="40" r="10" fill="var(--orange)"/><path d="M43 40l4 4 6-7" stroke="#fff" stroke-width="2.5" fill="none"/></svg>
    <h3>Secure<br>Transactions</h3>
    <p>Every listing is reviewed for<br>accuracy, with clear photos</p>
    <a>Read More</a>
  </div>
  <div class="feature" style="left:861px">
    <svg width="56" height="56" viewBox="0 0 56 56"><circle cx="28" cy="16" r="8" fill="var(--peach)"/><rect x="24" y="24" width="8" height="6" fill="var(--orange)"/><path d="M6 26v14l10 10h8V38l-10-10z" fill="var(--orange)"/><path d="M50 26v14l-10 10h-8V38l10-10z" fill="var(--orange-mid)"/></svg>
    <h3>Verified Collector<br>Listings</h3>
    <p>Every listing is reviewed for<br>accuracy, with clear photos</p>
    <a>Read More</a>
  </div>
</section>

<!-- centerpiece -->
<section class="centerpiece"></section>
<h2 class="abs h2 heading" style="left:111px;top:1178px">Find Your Next Centerpiece</h2>
<div class="rule" style="left:111px;top:1231px;width:475px;height:3px"></div>
<p class="body-copy" style="top:1263px">Step into a curated selection of standout diecast models chosen for their detail, rarity, and collector appeal. From timeless vintage classics to modern limited editions, each piece is showcased with high-quality images and transparent condition details — so you know exactly what you’re adding to your collection.</p>
<p class="body-copy" style="top:1415px">Discover a refined collection of diecast cars that define craftsmanship and rarity. Each model is carefully selected to meet the expectations of serious collectors — combining precision detail,</p>
<div class="btn" style="left:111px;top:1528px;width:230px;height:47px">Explore the Collection</div>
<div class="photo-red" role="img" aria-label="Red diecast pickup truck model lit in dark red light"></div>

<!-- featured -->
<h2 class="abs h2 heading" style="left:0;width:1200px;text-align:center;top:1735px">Featured Diecast Models</h2>
<div class="rule" style="left:488px;top:1794px;width:222px"></div>
<div class="product" style="left:111px"><div class="pic" role="img" aria-label="Red 1:24 scale sports coupe model"></div><h3>1:24 Diecast Model Car</h3><p class="sub">Precision crafted Rare find</p><p class="price">$89.99</p></div>
<div class="product" style="left:448px"><div class="pic" role="img" aria-label="Dark grey 1:24 scale finned custom car model"></div><h3>1:24 Scale Diecast Car</h3><p class="sub">Precision crafted Rare find</p><p class="price">$89.99</p></div>
<div class="product" style="left:784px"><div class="pic" role="img" aria-label="Yellow 1:24 scale hatchback rally car model"></div><h3>1:24 Scale Diecast</h3><p class="sub">Precision crafted Rare find</p><p class="price">$89.99</p></div>
<div class="btn" style="left:175px;top:2176px;width:177px;height:46px">Discover More</div>
<div class="btn" style="left:512px;top:2176px;width:177px;height:46px">Discover More</div>
<div class="btn" style="left:848px;top:2176px;width:177px;height:46px">Discover More</div>

<!-- cta -->
<section class="cta" role="img" aria-label="Faded row of model cars behind an orange overlay"></section>
<h2 class="abs heading" style="left:0;width:1200px;text-align:center;top:2384px;font-size:35px;color:var(--white)">Ready to Find Your Next Rare Piece?</h2>
<div class="rule" style="left:566px;top:2441px;width:146px;background:var(--white)"></div>
<p class="abs" style="left:0;width:1200px;text-align:center;top:2480px;font-size:15px;line-height:28px;color:var(--white)">Join a growing community of collectors buying, selling, and trading diecast cars every day. Discover rare finds, connect with<br>enthusiasts, and take your collection to the next level.</p>
<div class="btn" style="left:410px;top:2565px;width:177px;height:48px;background:var(--white);color:var(--orange)">Browse Listings</div>
<div class="btn" style="left:602px;top:2565px;width:195px;height:48px;background:transparent;border:2px solid var(--white)">List Your First Car</div>

<!-- testimonials -->
<h2 class="abs h2 heading" style="left:0;width:1200px;text-align:center;top:2774px">What Collectors Are Saying</h2>
<div class="rule" style="left:488px;top:2832px;width:222px"></div>
<div class="review" style="left:111px;width:474px"><span class="quote">“</span><h4>Marla</h4><div class="stars">★★★★★</div><p>“Finally a marketplace built for collectors. The listings are clear, the process is smooth, and I’ve already found rare models I couldn’t get anywhere else.”</p></div>
<div class="review" style="left:612px;width:477px"><span class="quote">“</span><h4>Theo Park</h4><div class="stars">★★★★★</div><p>“Selling my diecast cars was incredibly easy. I listed my models and connected with serious buyers within days. I love how transparent everything is. ”</p></div>

<!-- footer -->
<footer class="footer">
  <div class="f-brand">Vorlin<br>Diecast</div>
  <span class="social" style="left:131px"></span>
  <span class="social" style="left:163px"></span>
  <span class="social" style="left:196px"></span>
  <div class="f-col" style="left:377px"><h5>Quick Links</h5><ul><li>Home</li><li>Shop</li><li>Buy</li><li>Sell</li><li>Trade</li><li>Community</li><li>Blog</li></ul></div>
  <div class="f-col" style="left:594px"><h5>Customer Support</h5><ul><li>Contact Us</li><li>FAQs</li><li>Shipping &amp; Delivery</li><li>Returns &amp; Refunds</li><li>Help Center</li></ul></div>
  <div class="f-col f-contact" style="left:884px"><h5>Contact Us</h5>
    <div style="margin-top:14px"><svg width="16" height="16" viewBox="0 0 16 16"><circle cx="8" cy="8" r="8" fill="#fff"/><circle cx="8" cy="7" r="3" fill="var(--orange)"/></svg><span>48 Larkspur Avenue,<br>Fairhaven, NY 10027,</span></div>
    <div><svg width="16" height="16" viewBox="0 0 16 16"><circle cx="8" cy="8" r="8" fill="#fff"/><rect x="4" y="5" width="8" height="6" fill="var(--orange)"/></svg><span>info@halvanestudio.com</span></div>
    <div><svg width="16" height="16" viewBox="0 0 16 16"><circle cx="8" cy="8" r="8" fill="#fff"/><path d="M5 4l2 2-1 1 3 3 1-1 2 2-2 1c-3 0-6-3-6-6z" fill="var(--orange)"/></svg><span>+1 555 014 2290</span></div>
  </div>
  <div class="f-line"></div>
  <p class="f-bottom" style="left:111px">Privacy Policy &nbsp;| &nbsp;Terms &amp; Conditions &nbsp;| &nbsp;Cookie Policy</p>
  <p class="f-bottom" style="left:718px">© 2026 Halvane Studio. All rights reserved.</p>
</footer>

</body>
</html>
```